Platelet Rich Plasma (PRP) Flyer

Hi,

Looking to spruce up our Platelet Rich Plasma Flyer (see power point attachment). I also included previous flyers as examples on the design style we are looking for.

Quorum is our official font of our logo.
Attached is our logo in EPS format.
Please use the current photos in the power point. If you include photos, please make sure the stock image is free.

Files must be under 5MB. JPEG, PNG, PDF, .ai

Thank you,
Dorian

Target Market(s)

Patients

Industry/Entity Type

Healthcare

Font styles to use
Other font styles liked:
• Quorum

Requirements
Must have
• Emphasis on Platelet Rich Plasma Therapy when they pick up the flyer. The price of $199. FSA/HSA Eligible. The different treatment areas. The three addresses. Best of the best logo can be very small, not as important.
Nice to have
• One or two pictures. Less is more
Should not have
• Long paragraphs, multiple sentences.

```html
<!DOCTYPE html>
<html lang="en">
<head>
<meta charset="utf-8">
<title>Platelet Rich Plasma Therapy Flyer</title>
<link rel="stylesheet" href="https://fonts.googleapis.com/css2?family=Ubuntu:wght@400;500;700&family=Source+Sans+3:wght@400;600;700&family=Source+Serif+4:wght@400&display=swap">
<style>
  :root {
    --stage: #f2f2f2;
    --paper: #ececec;
    --teal: #13857a;
    --teal-band: #4fbfa8;
    --orange: #f07a43;
    --orange-dark: #e2602a;
    --phone: #c9471f;
    --green: #6fc79b;
    --leaf: #7cab2a;
    --ink: #222222;
    --footer: #e4e4e4;
    --blue: #5ab0e4;
    --charcoal: #4a4a4a;
    --white: #ffffff;
  }
  * { box-sizing: border-box; margin: 0; padding: 0; }
  html, body { width: 1200px; height: 1130px; overflow: hidden; background: var(--stage); }
  .flyer {
    position: absolute; left: 161px; top: 0;
    width: 865px; height: 1114px;
    background: var(--paper);
    transform: scale(1.0144); transform-origin: 0 0;
    overflow: hidden;
    font-family: "Source Sans 3", sans-serif;
    color: var(--ink);
  }
  .abs { position: absolute; }

  .hero-photo {
    left: 440px; top: 0; width: 425px; height: 290px;
    background: radial-gradient(ellipse at 70% 45%, #f4dccb 0%, #f6efe9 40%, #ececec 80%);
  }

  .brand { left: 70px; top: 56px; width: 412px; text-align: right; }
  .brand-mark {
    position: absolute; left: 20px; top: 30px; width: 70px; height: 70px;
    border-radius: 50%; background: var(--teal-band);
  }
  .brand-name {
    font-family: "Ubuntu", sans-serif; font-weight: 500; color: var(--orange);
    font-size: 40px; line-height: 42px; letter-spacing: 0.5px;
  }
  .brand-url {
    font-family: "Ubuntu", sans-serif; font-weight: 500; color: var(--orange);
    font-size: 18px; line-height: 22px;
  }

  .title {
    left: 50px; top: 230px;
    font-family: "Ubuntu", sans-serif; font-weight: 700; color: var(--teal);
    font-size: 53px; line-height: 54px; letter-spacing: -0.3px;
  }
  .title-rule { left: 50px; top: 346px; width: 612px; height: 2px; background: #9a9a9a; }

  .treating-badge { left: 33px; top: 361px; }
  .treating-list {
    left: 215px; top: 360px;
    font-family: "Ubuntu", sans-serif; font-size: 23px; color: #3a3a3a; line-height: 32px;
  }
  .treating-list span { display: inline-flex; align-items: center; margin-right: 14px; }
  .treating-list i {
    display: inline-block; width: 16px; height: 13px; border-radius: 50%;
    background: radial-gradient(circle at 35% 35%, #b6d95a, var(--leaf) 70%);
    margin-right: 10px;
  }

  .service-band { left: 0; top: 440px; }
  .service-text {
    left: 58px; top: 451px; width: 594px; text-align: center;
    font-family: "Source Sans 3", sans-serif; font-size: 17px; font-weight: 700;
    color: var(--white); white-space: nowrap; letter-spacing: -0.1px;
  }

  .photo-lab {
    left: 0; top: 483px; width: 445px; height: 214px;
    background: linear-gradient(100deg, #2a3f7a 0%, #d8d4d2 30%, #f6c79e 60%, #f3e6da 100%);
  }
  .photo-knee {
    left: 445px; top: 483px; width: 420px; height: 214px;
    background: radial-gradient(ellipse at 45% 60%, #a54a3a 0%, #2c4f68 35%, #143247 100%);
  }
  .divider-band { left: 0; top: 697px; width: 865px; height: 10px;
    background: linear-gradient(90deg, var(--teal-band), #5bc4c9); }

  .offer-panel {
    left: 0; top: 707px; width: 445px; height: 305px;
    background: linear-gradient(135deg, #ece6e8 0%, #e5e2e6 50%, #dfe0e5 100%);
  }
  .ribbon { left: 45px; top: 730px; }
  .appointments {
    left: 0; top: 808px; width: 460px; text-align: center;
    font-family: "Source Sans 3", sans-serif; font-weight: 600;
  }
  .appointments h2 { font-size: 27px; line-height: 34px; font-weight: 600; }
  .appointments p { font-size: 21px; line-height: 28px; }
  .appointments .sep { color: var(--orange); font-weight: 400; }
  .on-call {
    left: 88px; top: 886px; width: 290px; height: 60px;
    background: var(--green); border: 2px solid #3f9c78; border-radius: 4px;
    box-shadow: 0 2px 4px rgba(0,0,0,0.3);
    text-align: center; font-family: "Source Sans 3", sans-serif; font-weight: 700;
    font-size: 21px; line-height: 23px; color: #123b33; padding-top: 5px;
  }
  .on-call b { font-size: 30px; }
  .phone {
    left: 0; top: 946px; width: 460px; text-align: center;
    font-family: "Source Sans 3", sans-serif; font-weight: 700;
    font-size: 46px; color: var(--phone); letter-spacing: 0.5px;
  }

  .about {
    left: 445px; top: 707px; width: 420px; height: 305px;
    background: var(--white); padding: 18px 52px 0 31px;
    font-family: "Source Serif 4", serif; font-size: 16.5px; line-height: 20.6px;
    color: #333; text-align: justify;
  }
  .about p + p { margin-top: 20.6px; }
  .about .eligible {
    margin-top: 10px; text-align: left;
    font-family: "Source Sans 3", sans-serif; font-weight: 700; font-size: 17px;
    color: var(--teal);
  }

  .footer { left: 0; top: 1012px; width: 865px; height: 76px; background: var(--footer); }
  .office { top: 1020px; display: flex; gap: 12px; }
  .office svg { flex: none; margin-top: 2px; }
  .office h3 { font-size: 15px; font-weight: 700; line-height: 19px; }
  .office p { font-size: 13px; line-height: 16px; color: var(--ink); }
  .office-divider { top: 1024px; width: 1px; height: 44px; background: #8a8a8a; }

  .stripes { left: 0; top: 1088px; }
</style>
</head>
<body>
<main class="flyer">

  <div class="abs hero-photo" role="img" aria-label="Photo of a doctor in a white coat examining a patient's bare foot"></div>

  <header class="abs brand">
    <span class="brand-mark" aria-hidden="true"></span>
    <div class="brand-name">STRIDEWELL<br>FOOT &amp; ANKLE</div>
    <div class="brand-url">STRIDEWELLFEET.COM</div>
  </header>

  <h1 class="abs title">PLATELET RICH<br>PLASMA THERAPY (PRP)</h1>
  <div class="abs title-rule"></div>

  <svg class="abs treating-badge" width="176" height="62" viewBox="0 0 176 62">
    <polygon points="12,0 156,0 176,31 156,62 0,62" fill="var(--orange)"/>
    <text x="18" y="40" font-family="Ubuntu, sans-serif" font-weight="700" font-size="26" fill="#fff">TREATING:</text>
  </svg>
  <div class="abs treating-list">
    <div><span><i></i>Plantar Fasciitis</span><span><i></i>Achilles Tendonitis</span></div>
    <div><span><i></i>Tendon &amp; Ligament Injuries</span></div>
  </div>

  <svg class="abs service-band" width="865" height="45" viewBox="0 0 865 45">
    <rect x="0" y="34" width="865" height="9" fill="var(--teal-band)"/>
    <defs>
      <linearGradient id="bandGrad" x1="0" y1="0" x2="0" y2="1">
        <stop offset="0" stop-color="#f58a52"/><stop offset="1" stop-color="var(--orange-dark)"/>
      </linearGradient>
    </defs>
    <path d="M38,43 L58,6 Q62,0 70,0 L640,0 Q648,0 652,6 L672,43 Z" fill="url(#bandGrad)"/>
  </svg>
  <div class="abs service-text">PODIATRY | FOOT &amp; ANKLE SURGERY&nbsp; SPORTS MEDICINE | WOUND CARE</div>

  <div class="abs photo-lab" role="img" aria-label="Photo of gloved hands loading blood sample tubes into a centrifuge"></div>
  <div class="abs photo-knee" role="img" aria-label="Photo of a person holding a painful, red-highlighted knee against a dark blue background"></div>
  <div class="abs divider-band"></div>

  <div class="abs offer-panel" role="img" aria-label="Soft pale background photo of a medical injection"></div>

  <svg class="abs ribbon" width="380" height="78" viewBox="0 0 380 78">
    <defs>
      <linearGradient id="ribbonGrad" x1="0" y1="0" x2="0" y2="1">
        <stop offset="0" stop-color="#d9262b"/><stop offset="1" stop-color="#a5141a"/>
      </linearGradient>
    </defs>
    <path d="M108,28 L112,8 Q114,4 120,4 L260,4 Q266,4 268,8 L272,28 Z" fill="url(#ribbonGrad)"/>
    <text x="190" y="26" text-anchor="middle" font-family="Source Sans 3, sans-serif" font-weight="600" font-size="21" fill="#fff">SELF PAY PRICE</text>
    <path d="M0,72 L20,30 Q23,26 30,26 L350,26 Q357,26 360,30 L380,72 Z" fill="url(#ribbonGrad)"/>
    <text x="190" y="61" text-anchor="middle" font-family="Source Sans 3, sans-serif" font-weight="700" font-size="32" fill="#fff">$199 PER TREATMENT</text>
  </svg>

  <div class="abs appointments">
    <h2>APPOINTMENTS:</h2>
    <p>Same Day <span class="sep">|</span> Emergency <span class="sep">|</span> Saturday.</p>
  </div>
  <div class="abs on-call">OUR DOCTORS ARE ON<br>CALL AT THE SMC ER <b>24/7</b></div>
  <div class="abs phone">(877) 555-0142</div>

  <section class="abs about" aria-label="About PRP">
    <p>Platelet-rich plasma, or PRP is a substance that helps promote healing when injected. The platelets are the component of your own blood that contains special “factors,” or proteins, that help accelerate tissue repair and regeneration. It also contains proteins that support cell growth.</p>
    <p>Injecting the PRP into damaged tissues will stimulate your body to produce new, healthy cells and promote healing. A consultation is required to make sure you qualify.</p>
    <p class="eligible">FSA/HSA Eligible</p>
  </section>

  <footer class="abs footer"></footer>

  <div class="abs office" style="left:58px;">
    <svg width="30" height="48" viewBox="0 0 30 48"><path d="M15,0 C6.7,0 0,6.7 0,15 C0,26 15,48 15,48 C15,48 30,26 30,15 C30,6.7 23.3,0 15,0 Z" fill="#e33524"/><circle cx="15" cy="15" r="7" fill="#fff"/></svg>
    <div><h3>Northgate Office</h3><p>58 Linden Park Dr. Ste. 110<br>Northgate, MD 21000</p></div>
  </div>
  <div class="abs office-divider" style="left:322px;"></div>
  <div class="abs office" style="left:347px;">
    <svg width="30" height="48" viewBox="0 0 30 48"><path d="M15,0 C6.7,0 0,6.7 0,15 C0,26 15,48 15,48 C15,48 30,26 30,15 C30,6.7 23.3,0 15,0 Z" fill="#e33524"/><circle cx="15" cy="15" r="7" fill="#fff"/></svg>
    <div><h3>Riverside Office</h3><p>240 Mill Creek Road<br>Riverside, WV 25000</p></div>
  </div>
  <div class="abs office-divider" style="left:558px;"></div>
  <div class="abs office" style="left:587px;">
    <svg width="30" height="48" viewBox="0 0 30 48"><path d="M15,0 C6.7,0 0,6.7 0,15 C0,26 15,48 15,48 C15,48 30,26 30,15 C30,6.7 23.3,0 15,0 Z" fill="#e33524"/><circle cx="15" cy="15" r="7" fill="#fff"/></svg>
    <div><h3>Hillcrest Office</h3><p>7710 Oakmont Blvd. Ste. 305<br>Hillcrest, MD 21099</p></div>
  </div>

  <svg class="abs stripes" width="865" height="26" viewBox="0 0 865 26">
    <polygon points="0,0 152,0 140,26 0,26" fill="var(--teal-band)"/>
    <polygon points="152,0 322,0 310,26 140,26" fill="var(--orange)"/>
    <polygon points="322,0 490,0 478,26 310,26" fill="var(--charcoal)"/>
    <polygon points="490,0 668,0 656,26 478,26" fill="var(--green)"/>
    <polygon points="668,0 865,0 865,26 656,26" fill="var(--blue)"/>
  </svg>
</main>
</body>
</html>
```